Birchway MD Medical Practice Business Card

This business card is to represent my medical practice, which is a Concierge Primary Care Practice, in South Florida (USA.)
I'd like the designer to leave a space for the Office Address & Phone Number as I have not yet chosen these items.
I'd like to have a QR code on the back of the card that links to www.TheBirchwayMD.example.
I'd like the theme of the card to match my Logo (which should appear on the front of the card in some way.)
Please include my name on the card "Rosalind Pettibone, M.D." with the Title of CEO.
The front of the card should only have the logo (Birchway MD) and be blue.

Target Market(s)

My target clientele is ages 25-64, upper-middle class/affluent population and both male & female.

Industry/Entity Type

Medical / Doctor's Office

Contact Information for Business Card

ONLY HORIZONTAL layout. Save a spot for business address & phone #. I'd also like a QR code on the back that links to www.TheBirchwayMD.example.

Font styles to use
Other font styles liked:
• Match the Logo

Colors

Designer to choose colors to be used in the design.

Requirements
Must have
• Aforementioned + Email Address Welcome@TheBirchwayMD.example (written just like that)
Should not have
• Minimal to no black coloring.

```html
<!DOCTYPE html>
<html lang="en">
<head>
<meta charset="utf-8">
<title>Birchway MD – Business Card</title>
<link rel="stylesheet" href="https://fonts.googleapis.com/css2?family=Cinzel:wght@700&family=Poppins:wght@400&display=swap">
<style>
  :root {
    --backdrop: #6b6b6b;
    --card-blue: #00008a;
    --gold: #e8bb00;
    --gold-deep: #c08f10;
    --white: #ffffff;
  }
  * { box-sizing: border-box; margin: 0; padding: 0; }
  html, body { width: 1093px; height: 1200px; overflow: hidden; }
  body { background: var(--backdrop); position: relative; font-family: "Poppins", sans-serif; }
  .card {
    position: absolute;
    background: var(--card-blue);
    border-radius: 27px;
    overflow: hidden;
    box-shadow: 3px 4px 3px rgba(0, 0, 0, 0.45);
  }
  .card--front { left: 265px; top: 226px; width: 578px; height: 356px; }
  .card--back  { left: 265px; top: 621px; width: 582px; height: 357px; }

  .artwork-area {
    position: absolute; left: 281px; top: 0; width: 297px; height: 356px;
    background: radial-gradient(ellipse at 62% 48%, rgba(232, 187, 0, 0.30) 0%, rgba(192, 143, 16, 0.14) 45%, rgba(0, 0, 138, 0) 72%);
  }

  .holder { position: absolute; left: 27px; top: 74px; }
  .holder__name {
    font-family: "Cinzel", serif; font-weight: 700;
    color: var(--gold); font-size: 21px; line-height: 24px; letter-spacing: 0.2px;
    white-space: nowrap;
  }
  .holder__title { color: var(--white); font-size: 16.5px; line-height: 20px; }

  .contact { position: absolute; left: 27px; top: 165px; list-style: none; }
  .contact__item {
    display: flex; align-items: center; gap: 6px;
    color: var(--white); font-size: 16.5px; line-height: 21px; white-space: nowrap;
  }
  .contact__icon { width: 16px; height: 16px; flex: none; }

  .address {
    position: absolute; left: 27px; top: 279px;
    color: var(--white); font-size: 16.5px; line-height: 21px; font-style: normal;
  }

  .brand {
    position: absolute; left: 0; right: 0; top: 68px;
    display: flex; flex-direction: column; align-items: center;
  }
  .brand__dot {
    width: 150px; height: 150px; border-radius: 50%;
    border: 4px solid var(--gold);
  }
  .brand__name {
    margin-top: 20px;
    font-family: "Cinzel", serif; font-weight: 700;
    color: var(--white); font-size: 42px; line-height: 48px; letter-spacing: 0.5px;
  }

  .qr-slot {
    position: absolute; right: 22px; bottom: 22px; width: 56px; height: 56px;
    background: var(--white); border-radius: 4px;
  }
</style>
</head>
<body>

<section class="card card--front">
  <div class="artwork-area" role="img" aria-label="Large gold line artwork bleeding off the right edge of the card"></div>

  <div class="holder">
    <p class="holder__name">ROSALIND PETTIBONE, M.D.</p>
    <p class="holder__title">CEO</p>
  </div>

  <ul class="contact">
    <li class="contact__item">
      <svg class="contact__icon" viewBox="0 0 16 16" aria-hidden="true">
        <path d="M4 1.5l2.3 3-1.4 1.6c.8 1.9 2.2 3.3 4.2 4.3l1.6-1.4 3 2.3-1.3 2.6C7 13.4 2.4 8.9 1.5 3.1z" fill="var(--gold)"/>
      </svg>
      044-555 010 204
    </li>
    <li class="contact__item">
      <svg class="contact__icon" viewBox="0 0 16 16" aria-hidden="true">
        <rect x="0.5" y="3" width="15" height="10.5" fill="var(--gold)"/>
        <path d="M1 3.6l7 5.4 7-5.4" fill="none" stroke="var(--card-blue)" stroke-width="1.2"/>
      </svg>
      Welcome@TheBirchwayMD.example
    </li>
    <li class="contact__item">
      <svg class="contact__icon" viewBox="0 0 16 16" aria-hidden="true">
        <g fill="none" stroke="var(--gold)" stroke-width="1.4">
          <circle cx="8" cy="8" r="6.6"/>
          <ellipse cx="8" cy="8" rx="3" ry="6.6"/>
          <path d="M1.6 6h12.8M1.6 10h12.8"/>
        </g>
      </svg>
      www.TheBirchwayMD.example
    </li>
  </ul>

  <address class="address">
    421, Address line goes here<br>
    45452,Country Name
  </address>
</section>

<section class="card card--back">
  <div class="brand">
    <span class="brand__dot" aria-hidden="true"></span>
    <p class="brand__name">BIRCHWAY MD</p>
  </div>
  <div class="qr-slot" role="img" aria-label="QR code linking to www.TheBirchwayMD.example"></div>
</section>

</body>
</html>
```